Business card for Mortgage broker business

I have already had the logo designed and am needing a great looking business card. My business focus is on servicing clients who may not be able to obtain finance through traditional lenders due to bad credit, short term employment or they just don't fit the banks profile. It needs to be professional, trust worthy but also have a caring fell about it.
I have provided files showing the green and black logo, the white logo(on white background so the file looks blank) and also a file with the white logo with a background of leaves that was made up which will probably be used for a website header.

Industry/Entity Type

Finance

Contact Information for Business Card

Marcus Dalby
Managing Director, Accredited Finance Broker(AFB)
Po Box 817, Larkfield VIC 3842
marcus@kestrelfunding.com.au
www.kestrelfunding.com.au
0438 216 507

Requirements
Nice to have
• I have added a picture of myself as I would like to see some designs with the pic in it, but I'm not sure if I want it on there with the logo's or just the logo's

```html
<!DOCTYPE html>
<html lang="en">
<head>
<meta charset="utf-8">
<title>Kestrel Funding – Business Card</title>
<link rel="stylesheet" href="https://fonts.googleapis.com/css2?family=Lato:wght@400;700&family=Noto+Serif:wght@400&display=swap">
<style>
  :root {
    --page-top: #cbcbcb;
    --page-bottom: #5c5c5c;
    --front-top: #0f0f11;
    --front-bottom: #4d4d4f;
    --band-light-top: #f8f8fa;
    --band-light-bottom: #ececf1;
    --band-dark-top: #2a2a2c;
    --band-dark-bottom: #4a4a4c;
    --ink-light: #ffffff;
    --ink-dark: #3e3e42;
    --ink-muted: #7b7b7f;
    --icon-disc: #ececf0;
  }
  * { margin: 0; padding: 0; box-sizing: border-box; }
  html, body { width: 1149px; height: 1200px; overflow: hidden; }
  body {
    background: linear-gradient(to bottom, var(--page-top), var(--page-bottom));
    font-family: "Lato", sans-serif;
    position: relative;
  }
  .card {
    position: absolute;
    left: 199px;
    width: 754px;
    height: 433px;
    overflow: hidden;
  }
  .card--front {
    top: 127px;
    background: linear-gradient(to bottom, var(--front-top), var(--front-bottom));
  }
  .card--back { top: 620px; }

  .wordmark {
    position: absolute;
    left: 0; right: 0;
    text-align: center;
    font-family: "Lato", sans-serif;
    font-weight: 400;
    letter-spacing: 2px;
    white-space: nowrap;
  }
  .card--front .wordmark {
    top: 170px;
    font-size: 62px;
    color: var(--ink-light);
  }

  .identity-band {
    position: absolute;
    left: 0; top: 0;
    width: 100%; height: 206px;
    background: linear-gradient(to bottom, var(--band-light-top), var(--band-light-bottom));
  }
  .holder-name {
    position: absolute;
    left: 11px; top: 4px;
    font-family: "Noto Serif", serif;
    font-size: 27px;
    color: var(--ink-muted);
  }
  .holder-title {
    position: absolute;
    left: 11px; top: 40px;
    font-size: 12.5px;
    color: var(--ink-muted);
  }
  .identity-band .wordmark {
    top: 98px;
    font-size: 44px;
    color: var(--ink-dark);
    padding-left: 20px;
  }

  .contact-band {
    position: absolute;
    left: 0; top: 206px;
    width: 100%; height: 227px;
    background: linear-gradient(to bottom, var(--band-dark-top), var(--band-dark-bottom));
  }
  .contact-item {
    position: absolute;
    display: flex;
    align-items: center;
    gap: 13px;
    color: var(--ink-light);
    font-weight: 700;
    font-size: 16.5px;
    white-space: nowrap;
  }
  .contact-item--address { left: 30px; top: 51px; }
  .contact-item--phone   { left: 387px; top: 51px; }
  .contact-item--web     { left: 26px; top: 133px; }
  .contact-item--email   { left: 387px; top: 133px; }
  .contact-icon {
    width: 44px; height: 44px;
    border-radius: 50%;
    background: var(--icon-disc);
    display: flex; align-items: center; justify-content: center;
    flex: none;
  }
  .contact-icon svg { width: 24px; height: 24px; }
</style>
</head>
<body>

  <section class="card card--front" aria-label="Card front">
    <div class="wordmark">Kestrel Funding</div>
  </section>

  <section class="card card--back" aria-label="Card back">
    <div class="identity-band">
      <div class="holder-name">Marcus Dalby</div>
      <div class="holder-title">Managing Director, Accredited Finance Broker(AFB)</div>
      <div class="wordmark">Kestrel Funding</div>
    </div>

    <div class="contact-band">
      <div class="contact-item contact-item--address">
        <span class="contact-icon">
          <svg viewBox="0 0 24 24" fill="none" stroke="#3e3e42" stroke-width="1.8">
            <path d="M12 3a5 5 0 0 0-5 5c0 4 5 9 5 9s5-5 5-9a5 5 0 0 0-5-5z"/>
            <circle cx="12" cy="8" r="1.8"/>
            <path d="M7 17.5c-2 .5-3 1.2-3 2 0 1.4 3.6 2 8 2s8-.6 8-2c0-.8-1-1.5-3-2"/>
          </svg>
        </span>
        <span>Po Box 817, Larkfield VIC 3842</span>
      </div>

      <div class="contact-item contact-item--phone">
        <span class="contact-icon">
          <svg viewBox="0 0 24 24" fill="none" stroke="#3e3e42" stroke-width="1.8">
            <path d="M7 4l3 4-2 2c1 2 3 4 5 5l2-2 4 3-2 3c-6 0-12-6-12-12z" fill="#3e3e42"/>
            <path d="M14 4a6 6 0 0 1 6 6M14 7.5a2.5 2.5 0 0 1 2.5 2.5"/>
          </svg>
        </span>
        <span>0438 216 507</span>
      </div>

      <div class="contact-item contact-item--web">
        <span class="contact-icon">
          <svg viewBox="0 0 24 24" fill="none" stroke="#3e3e42" stroke-width="1.6">
            <circle cx="12" cy="12" r="8.5"/>
            <ellipse cx="12" cy="12" rx="3.8" ry="8.5"/>
            <path d="M3.5 12h17M5 7.5h14M5 16.5h14"/>
          </svg>
        </span>
        <span>www.kestrelfunding.com.au</span>
      </div>

      <div class="contact-item contact-item--email">
        <span class="contact-icon">
          <svg viewBox="0 0 24 24" fill="#3e3e42">
            <path d="M3 9l9 6 9-6v10H3z"/>
            <path d="M3 8l9-5 9 5-9 6z" fill="none" stroke="#3e3e42" stroke-width="1.6"/>
          </svg>
        </span>
        <span>marcus@kestrelfunding.com.au</span>
      </div>
    </div>
  </section>

</body>
</html>
```